Property Management Company

We are looking for a sharp/modern business card design for a property management company.
We have included what should be on the business card down below in business card details.
Target Market(s)
Commercial properties, Home Owners
Industry/Entity Type
Business
Contact Information for Business Card
Name: Dale Orsino | Owner
Business Name : Kestrel Yards
Slogan : A Smarter Choice
Phone : 555.304.8862
Website: www.kestrelyards.example
E-Mail : dale@kestrelyards.example
Our Services are Commercial & Residential
-Asphalt Maintenance
-Snow Management
-Landscaping
-Blacktop
Free Estimates
Free parking lot cleanup & restripe with snow removal contract
Look and feel

```html
<!DOCTYPE html>
<html lang="en">
<head>
<meta charset="utf-8">
<title>Kestrel Yards – Business Card</title>
<link href="https://fonts.googleapis.com/css2?family=Open+Sans:ital,wght@0,400;0,600;0,700;0,800;1,400;1,600&display=swap" rel="stylesheet">
<style>
  :root{
    --navy:#25356b;
    --red:#d3344a;
    --green:#1c8b4c;
    --green-dark:#157a40;
    --ink:#222;
    --paper:#ffffff;
    --stage:#e9e7e3;
    --rule:#8a8a8a;
  }
  *{box-sizing:border-box;margin:0;padding:0}
  html,body{width:1200px;height:1000px;overflow:hidden}
  body{background:var(--stage);font-family:"Open Sans",Arial,sans-serif;color:var(--ink);position:relative}
  .card{position:absolute;left:250px;width:700px;height:400px;background:var(--paper);border-radius:22px;box-shadow:0 6px 18px rgba(0,0,0,.15);overflow:hidden}
  .card--front{top:50px;display:flex;flex-direction:column;align-items:center;justify-content:center;gap:18px}
  .card--back{top:530px}

  .brand{display:flex;align-items:center;gap:16px}
  .brand__dot{width:34px;height:34px;border-radius:50%;background:var(--navy)}
  .brand__name{font-weight:800;font-size:64px;color:var(--navy);letter-spacing:.5px;line-height:1}
  .slogan{font-size:20px;font-weight:600;letter-spacing:4px;text-transform:uppercase;color:var(--green)}

  .back__top{position:absolute;left:0;top:0;width:700px;height:190px;display:flex;align-items:center;padding:0 44px}
  .back__brand{flex:1;display:flex;align-items:center;gap:12px}
  .back__brand .brand__dot{width:22px;height:22px}
  .back__brand .brand__name{font-size:38px}
  .divider{width:1px;height:120px;background:var(--rule);margin:0 34px}
  .contact{flex:1}
  .contact__name{font-weight:800;font-size:26px;text-transform:uppercase;letter-spacing:.5px;line-height:1.1}
  .contact__role{font-size:17px;color:var(--green);font-weight:600;margin-bottom:10px}
  .contact__row{display:flex;align-items:center;gap:8px;font-size:16px;font-weight:600;line-height:1.55}
  .contact__row svg{width:15px;height:15px;flex:none}

  .services__head{position:absolute;left:0;top:196px;width:700px;height:40px;background:var(--navy);color:#fff;font-weight:600;font-size:17px;letter-spacing:2px;display:flex;align-items:center;justify-content:center;text-transform:uppercase}
  .services{position:absolute;left:0;top:236px;width:700px;height:164px;background:linear-gradient(180deg,var(--green),var(--green-dark));color:#fff;display:flex;flex-direction:column;justify-content:center;align-items:center;gap:8px;font-style:italic;font-size:19px}
  .services__line{display:flex;gap:14px;align-items:center}
  .services__item{display:inline-flex;align-items:center;gap:6px}
  .tick{width:14px;height:12px}
</style>
</head>
<body>

<section class="card card--front" aria-label="Card front">
  <div class="brand">
    <span class="brand__dot"></span>
    <span class="brand__name">Kestrel Yards</span>
  </div>
  <p class="slogan">A Smarter Choice</p>
</section>

<section class="card card--back" aria-label="Card back">
  <div class="back__top">
    <div class="back__brand">
      <span class="brand__dot"></span>
      <span class="brand__name">Kestrel Yards</span>
    </div>
    <div class="divider"></div>
    <div class="contact">
      <p class="contact__name">Dale Orsino</p>
      <p class="contact__role">Owner</p>
      <p class="contact__row">
        <svg viewBox="0 0 16 16"><rect x="4" y="1" width="8" height="14" rx="1.5" fill="var(--green)"/><rect x="5.5" y="3" width="5" height="8" fill="#fff"/></svg>
        555.304.8862
      </p>
      <p class="contact__row">
        <svg viewBox="0 0 16 16"><rect x="1" y="3" width="14" height="10" rx="1" fill="var(--green)"/><path d="M1.5 3.5 8 9l6.5-5.5" stroke="#fff" stroke-width="1.4" fill="none"/></svg>
        dale@kestrelyards.example
      </p>
      <p class="contact__row">
        <svg viewBox="0 0 16 16"><circle cx="8" cy="8" r="7" fill="var(--green)"/><path d="M1 8h14M8 1c-3 3-3 11 0 14M8 1c3 3 3 11 0 14" stroke="#fff" stroke-width="1" fill="none"/></svg>
        www.kestrelyards.example
      </p>
    </div>
  </div>

  <div class="services__head">Our Services</div>
  <div class="services">
    <p class="services__line">
      <span class="services__item">Commercial &amp; Residential <svg class="tick" viewBox="0 0 14 12"><path d="M1 6l4 4 8-9" stroke="var(--red)" stroke-width="2.4" fill="none"/></svg></span>
      <span class="services__item">Asphalt Maintenance <svg class="tick" viewBox="0 0 14 12"><path d="M1 6l4 4 8-9" stroke="var(--red)" stroke-width="2.4" fill="none"/></svg></span>
      <span class="services__item">Free Estimates <svg class="tick" viewBox="0 0 14 12"><path d="M1 6l4 4 8-9" stroke="var(--red)" stroke-width="2.4" fill="none"/></svg></span>
    </p>
    <p class="services__line">
      <span class="services__item">Snow Management <svg class="tick" viewBox="0 0 14 12"><path d="M1 6l4 4 8-9" stroke="var(--red)" stroke-width="2.4" fill="none"/></svg></span>
      <span class="services__item">Landscaping <svg class="tick" viewBox="0 0 14 12"><path d="M1 6l4 4 8-9" stroke="var(--red)" stroke-width="2.4" fill="none"/></svg></span>
      <span class="services__item">Blacktop <svg class="tick" viewBox="0 0 14 12"><path d="M1 6l4 4 8-9" stroke="var(--red)" stroke-width="2.4" fill="none"/></svg></span>
    </p>
    <p class="services__line">
      <span class="services__item">Free parking lot cleanup &amp; restripe with snow removal contract <svg class="tick" viewBox="0 0 14 12"><path d="M1 6l4 4 8-9" stroke="var(--red)" stroke-width="2.4" fill="none"/></svg></span>
    </p>
  </div>
</section>

</body>
</html>
```